Cover design needed for scholarship book whose intended audience is students with medical conditions

I need a book cover designed for a book called, “The Thistle Grant: Ways To Change Your Health Challenge Into Open Funds For University.” This book is aimed at students with a variety of medical conditions. I wrote The Thistle Grant after I received a medical-based scholarship ($96,000) to attend college and law school based on my allergies to pollen—hence the title. However, this government program applies to just about any medical condition—not just allergies. I have assisted students in applying for this program who suffer from many different medical conditions. So I would like the cover design to convey that message—that this program applies to many different medical conditions. One of the big misconceptions about medical-based scholarships is you will only qualify if you have a really serious medical condition. So I would like to see some cover designs that list some common medical conditions in order to convey to the reader that many different medical conditions qualify. A few possible medical conditions are allergies, asthma, ADHD, depression, anxiety, back pain, eating disorders, bipolar, sleep disorders, and OCD. Possible ways to convey this may be to have the names of some of these common medical conditions written on graduation caps or randomly dispersed in the background, etc. However, this isn’t the only theme I would like to see. In essence, I give you creative liberty to wow me with your design prowess. The point of crowd design is to get variety of designs to choose from that I may not have thought of on my own. I have dabbled with some ideas that blend the themes of the education world and the medical world and I think this is the essence of the book. What ever you come up with, it needs to make it clear at a glance that this book helps you pay for college on the basis of your medical condition—whatever medical condition that may be. To see a simple mock up I did (that I don't want to use) go to healthawardfinder.example

The book is 153 pages on 5x8 paper. I am planning to print the book through PageForge, so the cover should adhere to the PageForge design requirements. I can provide the PageForge template if needed.

Updates: Please be able to provide a few updates to the cover design if your design is selected. After choosing the final design, physical proofs of the book will be ordered so I can see what your design looks like in real life. After the proofs are reviewed, I may need some minor changes (i.e., maybe the back cover text needs a new font size, etc..) Also, after I use the proofs to solicit endorsements, I am planning to purchase my own ISBN number and barcode. I would like the designer to be able to update my cover to include a new ISBN and barcode after the initial proofs are printed which should be 3-4 weeks later. So please be able to provide a few updates to the cover design if your design is selected.

Target Market(s)

Students/parents who are planning to attend college and have some type of medical condition

Industry/Entity Type

College

Font styles to use
Serif

Requirements
Must have
• My project must have a general education/medical theme
Nice to have
• I'd like to see some designs that include random medical conditions dispersed on the cover. Maybe a different medical condition written on several different graduation caps, or some other context.
Should not have
• The cover design should not depict persons with severe medical conditions--i.e., people in wheelchairs, hospital beds, etc.

```html
<!DOCTYPE html>
<html lang="en">
<head>
<meta charset="utf-8">
<title>The Thistle Grant – Book Cover</title>
<link rel="stylesheet" href="https://fonts.googleapis.com/css2?family=Tinos:wght@400;700&display=swap">
<style>
  :root {
    --maroon-deep: #2a0703;
    --maroon: #5a1208;
    --maroon-glow: #7a2410;
    --cream: #f1e6d6;
    --gold: #dba85c;
    --ink: #140c06;
    --sky-top: #a27a4a;
    --sky-mid: #c79a5e;
    --sun: #f3d49a;
    --night: #0a0604;
  }
  * { margin: 0; padding: 0; box-sizing: border-box; }
  html, body { width: 1200px; height: 881px; overflow: hidden; background: var(--night); }
  .cover {
    position: relative; width: 1200px; height: 881px; overflow: hidden;
    font-family: "Tinos", "Times New Roman", serif;
  }

  /* Back cover */
  .back {
    position: absolute; left: 0; top: 0; width: 618px; height: 881px;
    background: radial-gradient(ellipse at 55% 40%, var(--maroon-glow) 0%, var(--maroon) 40%, var(--maroon-deep) 100%);
    color: var(--cream);
  }
  .back-heading {
    position: absolute; left: 34px; top: 152px; width: 540px;
    text-align: center; font-weight: 700; font-size: 20.5px; line-height: 26px;
  }
  .rule { position: absolute; left: 34px; width: 541px; height: 1.5px; background: var(--cream); }
  .rule-top { top: 210px; }
  .rule-bio-top { top: 525px; }
  .rule-bio-bottom { top: 673px; }
  .blurb {
    position: absolute; left: 33px; top: 222px; width: 528px;
    font-size: 15.2px; line-height: 19.3px; text-align: justify;
  }
  .author-photo {
    position: absolute; left: 34px; top: 526px; width: 148px; height: 147px;
    background: linear-gradient(160deg, #7d8a5e 0%, #b9b3a0 45%, #e7e8ec 100%);
    border: 2px solid var(--cream);
  }
  .author-bio {
    position: absolute; left: 201px; top: 532px; width: 360px;
    font-size: 15.2px; line-height: 19.3px; text-align: justify;
  }

  /* Spine */
  .spine {
    position: absolute; left: 576px; top: 0; width: 42px; height: 881px;
    color: var(--cream);
  }
  .spine-title, .spine-author {
    position: absolute; left: 4px; writing-mode: vertical-rl;
    font-size: 33px; line-height: 34px; letter-spacing: 0.5px; white-space: nowrap;
  }
  .spine-title { top: 42px; }
  .spine-author { top: 600px; }

  /* Front cover */
  .front { position: absolute; left: 618px; top: 0; width: 582px; height: 881px; background: var(--night); }
  .front-scene {
    position: absolute; left: 0; top: 0; width: 582px; height: 578px;
    background:
      radial-gradient(ellipse 180px 150px at 310px 470px, var(--sun) 0%, rgba(230,160,80,0.55) 45%, rgba(0,0,0,0) 100%),
      linear-gradient(180deg, var(--sky-top) 0%, var(--sky-mid) 35%, #8a5a2c 60%, #1c0f08 82%, var(--night) 100%);
  }
  .front-title {
    position: absolute; left: 0; top: 38px; width: 582px; text-align: center;
    color: var(--ink); font-size: 82px; line-height: 76px; letter-spacing: 1px;
  }
  .cap-label {
    position: absolute; color: #fff; font-family: Arial, Helvetica, sans-serif;
    font-size: 14px; white-space: nowrap; transform-origin: left center;
  }
  .subtitle {
    position: absolute; left: 0; top: 601px; width: 582px; text-align: center;
    color: var(--gold); font-size: 36px; line-height: 41px;
  }
  .front-author {
    position: absolute; left: 0; top: 752px; width: 582px; text-align: center;
    color: var(--gold); font-size: 78px; line-height: 84px; letter-spacing: 1px;
  }
</style>
</head>
<body>
<div class="cover">

  <section class="back">
    <h2 class="back-heading">How Anyone Can Get Free Money for College<br>on the Basis of Their Medical Condition!</h2>
    <div class="rule rule-top"></div>
    <p class="blurb">The first book ever to expose the secret world of medical-based scholarships, The Thistle Grant shows you how to turn any medical condition into free money for college! Whether your medical condition is incredibly serious or just mildly annoying, this book can save you a fortune in college expenses! Medical-based scholarships provide students with an exciting opportunity to pay for college on the basis of just about any medical condition—allergies, ADHD, anxiety, depression, back pain—the list goes on and on. But to take advantage of this program, first you need to know how to apply!<br>The Thistle Grant is a step-by-step guide that walks students and parents through the simple application process for the medical-based scholarship program. It doesn’t matter where you live, what college you plan to attend, or what medical condition you suffer from, The Thistle Grant applies to you! With the ever-increasing cost of a college education, if you suffer from any medical condition whatsoever, The Thistle Grant is a must read!</p>
    <div class="rule rule-bio-top"></div>
    <div class="author-photo" role="img" aria-label="Portrait photo of the author outdoors among trees"></div>
    <p class="author-bio">Daniel Hart is an attorney–author who received $96,000 through the medical-based scholarship program on the basis of his medical conditions of asthma and thistle allergies (hence the book’s title, The Thistle Grant). Daniel is a former Assistant Attorney General for the state of Florida. Daniel is currently an Attorney–Advisor for the US Office of Legal Review.</p>
    <div class="rule rule-bio-bottom"></div>
  </section>

  <section class="spine">
    <div class="spine-title">THE THISTLE GRANT</div>
    <div class="spine-author">DANIEL HART</div>
  </section>

  <section class="front">
    <div class="front-scene" role="img" aria-label="Silhouettes of four graduates in caps against a golden sunset sky"></div>
    <h1 class="front-title">THE THISTLE<br>GRANT</h1>

    <span class="cap-label" style="left:72px;top:314px;transform:rotate(-20deg)">Allergies</span>
    <span class="cap-label" style="left:86px;top:342px;transform:rotate(-20deg)">Asthma</span>
    <span class="cap-label" style="left:200px;top:336px;transform:rotate(-18deg)">Sleep disorders</span>
    <span class="cap-label" style="left:205px;top:362px;transform:rotate(-30deg)">Eating disorders</span>
    <span class="cap-label" style="left:362px;top:304px;transform:rotate(36deg)">Depression</span>
    <span class="cap-label" style="left:362px;top:326px;transform:rotate(36deg)">Anxiety</span>
    <span class="cap-label" style="left:472px;top:216px;transform:rotate(-6deg)">OCD</span>
    <span class="cap-label" style="left:463px;top:238px;transform:rotate(-10deg)">Back pain</span>

    <p class="subtitle">WAYS TO CHANGE YOUR<br>HEALTH CHALLENGE INTO<br>OPEN FUNDS FOR UNIVERSITY.</p>
    <p class="front-author">DANIEL HART</p>
  </section>

</div>
</body>
</html>
```